Lumo Habitat Real estate Costa del sol

we need a website for our Company based in Costa del sol, Spain. We sell properties on the spanish coast that is called costa del sol. We are concentrating on exclusive properties and would like the webdesign to show this. In our website we want to have area descriptions of the different areas we sell our Products. We will also implement a searchable database delivered by a third part where all properties for sale in Spain are listed. When looking into the designs we would like our main page to have a overview of the coast where the different areas are shown. Have a look at brightvillarow.com or mykelsa.com to see. The webpage will be presented in 4 languages, English, spanish, Swedish and norwegian, and shall of course also be prepared for social medias. We want an easy Contemporary design but still with an exclusive feeling!
Target Market(s)
Scandinavian and North european Citizens wants to buy a property in Spain
Industry/Entity Type
Real Estate
Number of Pages Required
5+ page
Look and feel

```html
<!DOCTYPE html>
<html lang="en">
<head>
<meta charset="utf-8">
<title>Lumo Habitat – High Tech Villa</title>
<link href="https://fonts.googleapis.com/css2?family=Cinzel:wght@400;700&family=Open+Sans:wght@400;600;700&display=swap" rel="stylesheet">
<style>
:root{
  --navy:#0d1440;
  --navy-soft:rgba(13,20,64,.9);
  --ink:#222;
  --muted:#555;
  --grey-panel:#9b9b9b;
  --light:#f3f3f3;
  --band:#e6e6e6;
  --dark:#1d1d1d;
  --footer:#262626;
  --white:#fff;
}
*{box-sizing:border-box;margin:0;padding:0}
html,body{width:1200px;height:3333px;overflow:hidden}
body{position:relative;background:var(--white);font-family:"Open Sans",Arial,sans-serif;color:var(--ink)}
.abs{position:absolute}

/* header */
.topnav{left:0;top:0;width:1200px;height:44px;background:var(--navy)}
.topnav a{position:absolute;top:13px;color:var(--white);font-family:"Cinzel",Georgia,serif;font-size:16px;letter-spacing:1px;text-decoration:none}
.brand-cap{left:506px;top:0;width:188px;height:104px;background:var(--white);border-radius:94px 94px 0 0/60px 60px 0 0}
.brand{left:506px;top:18px;width:188px;text-align:center}
.brand .mark{display:block;margin:0 auto 6px;width:34px;height:34px;border:3px solid var(--navy)}
.brand .name{font-family:"Cinzel",Georgia,serif;font-size:20px;color:var(--navy)}
.lang{left:46px;top:66px;font-size:13px;color:var(--ink)}
.lang .select{display:inline-block;margin-left:10px;border:1px solid #ccc;padding:3px 10px;font-size:11px}
.social{top:63px;width:22px;height:22px;border:2px solid var(--ink);border-radius:50%}

/* hero */
.hero{left:0;top:107px;width:1200px;height:555px;background:linear-gradient(180deg,#9cc0e0 0%,#c9dbe8 35%,#6e8f9a 55%,#2f6c86 75%,#3e5b3a 100%)}
.hero-title{left:49px;top:276px;width:516px;height:157px;background:rgba(255,255,255,.32);padding:18px 28px}
.hero-title h1{font-family:"Cinzel",Georgia,serif;font-weight:400;font-size:46px;color:var(--navy);letter-spacing:2px}
.hero-title p{font-family:"Cinzel",Georgia,serif;font-size:24px;color:var(--navy);line-height:30px;margin-top:6px}
.consult{left:840px;top:155px;width:313px;height:481px;background:var(--navy-soft)}
.consult-head{position:absolute;left:0;top:0;width:313px;height:74px;background:var(--grey-panel);text-align:center;padding-top:8px;font-family:"Cinzel",Georgia,serif;color:var(--white);font-size:26px;line-height:30px}
.consult-head b{font-weight:700}
.consult label{position:absolute;font-size:13px;font-weight:600;color:var(--white);letter-spacing:.5px}
.consult .field{position:absolute;height:30px;background:var(--white);font-size:11px;color:#999;padding:8px 6px}
.consult-submit{position:absolute;left:0;bottom:0;width:313px;height:48px;background:var(--grey-panel);color:var(--white);text-align:center;font-family:"Cinzel",Georgia,serif;font-weight:700;font-size:20px;line-height:48px;letter-spacing:1px}
.ficon{left:810px;width:54px;height:52px;background:var(--grey-panel);display:flex;align-items:center;justify-content:center}

.notice{left:0;top:662px;width:1200px;height:82px;background:var(--band);font-size:16px;padding:30px 0 0 90px;color:var(--ink)}
.notice a{color:var(--navy);font-weight:700}
.notice svg{position:absolute;left:58px;top:30px}

/* about */
.ph-house{left:44px;top:793px;width:278px;height:460px;background:linear-gradient(160deg,#d8e3ec 0%,#e9ecee 45%,#8ea273 80%,#52683d 100%)}
.ph-frame{border:2px solid rgba(255,255,255,.9)}
.kicker{font-family:"Cinzel",Georgia,serif;font-size:15px;color:var(--ink)}
.section-title{font-family:"Cinzel",Georgia,serif;font-size:26px;color:var(--navy);letter-spacing:1.5px}
.rule{height:3px;background:var(--navy)}
.body-text{font-size:13.5px;line-height:23px;color:var(--muted)}
.room{width:130px;text-align:center}
.room .lbl{font-size:13px;font-weight:700;color:var(--ink);margin-top:12px}
.room .num{font-size:30px;font-style:italic;color:var(--ink);margin-top:8px;font-family:Georgia,serif}

/* highlights */
.hl-bg{left:502px;top:1313px;width:698px;height:391px;background:var(--light)}
.ph-bedroom{left:0;top:1313px;width:502px;height:391px;background:linear-gradient(135deg,#e9ecef 0%,#cfd3d6 50%,#7c6d66 80%,#3b3533 100%)}
.hl-item{width:260px}
.hl-item h4{font-family:"Cinzel",Georgia,serif;font-size:14px;font-weight:700;color:var(--ink);margin-bottom:6px;letter-spacing:.5px}
.hl-item p{font-size:12.5px;line-height:17px;color:var(--muted)}
.pin{width:38px;height:48px}

/* room dimensions */
.center{left:0;width:1200px;text-align:center}
.ph-balcony{left:100px;top:1924px;width:584px;height:365px;background:linear-gradient(180deg,#f2c48a 0%,#e59a55 35%,#8a6d5a 60%,#5e4b3f 100%)}
.size-tag{left:104px;top:2230px;width:112px;height:48px;background:var(--white);font-size:17px;font-weight:700;text-align:center;line-height:48px}
.balcony-box{left:649px;top:1960px;width:438px;height:291px;background:#eeeeee;border:1px solid #ddd;padding:40px 32px}
.balcony-box h3{font-family:"Cinzel",Georgia,serif;font-weight:400;font-size:24px;color:var(--ink);margin-bottom:14px}
.balcony-box p{font-size:14px;line-height:24px;color:#888}
.balcony-box li{list-style:none;font-size:11px;font-weight:700;color:var(--ink);margin-top:20px;letter-spacing:.3px}
.balcony-box ul{margin-top:6px}

/* contact */
.contact{left:0;top:2355px;width:1200px;height:432px;background:linear-gradient(90deg,#262626,#1a1a1a)}
.ph-agent{left:80px;width:249px;height:340px;background:linear-gradient(160deg,#a9b9c9 0%,#7a8ea5 50%,#4c5f7a 100%);border:4px solid var(--white)}
.contact .w{color:var(--white);font-family:"Cinzel",Georgia,serif}
.cf{left:793px;width:316px;height:30px;background:var(--white);font-size:11px;color:#999;padding:8px 10px;letter-spacing:.5px}
.send{left:793px;top:2720px;width:100px;height:36px;background:#8a8a8a;color:var(--white);font-family:"Cinzel",Georgia,serif;font-size:16px;text-align:center;line-height:36px}

.map{left:0;top:2787px;width:1200px;height:368px;background:linear-gradient(135deg,#ececec,#dfe3e6)}
.footer{left:0;top:3155px;width:1200px;height:178px;background:var(--footer)}
.footer .brand-f{left:70px;top:50px;text-align:center;color:var(--white)}
.footer .brand-f .mark{display:block;margin:0 auto 8px;width:40px;height:40px;border:3px solid #aaa}
.footer .brand-f .name{font-family:"Cinzel",Georgia,serif;font-size:22px}
.footer .copy{right:50px;top:83px;font-family:"Cinzel",Georgia,serif;font-size:13px;color:#888;letter-spacing:.5px}
</style>
</head>
<body>

<nav class="abs topnav">
  <a style="left:82px">Home</a>
  <a style="left:204px">Gallery</a>
  <a style="left:346px">Promotion</a>
  <a style="left:764px">Service</a>
  <a style="left:914px">Blog</a>
  <a style="left:1044px">Contact</a>
</nav>
<div class="abs brand-cap"></div>
<div class="abs brand"><span class="mark"></span><span class="name">Lumo Habitat</span></div>
<div class="abs lang">Languages <span class="select">ENGLISH ▾</span></div>
<span class="abs social" style="left:985px"></span>
<span class="abs social" style="left:1015px"></span>
<span class="abs social" style="left:1045px"></span>
<span class="abs social" style="left:1075px"></span>
<span class="abs social" style="left:1105px"></span>

<div class="abs hero" role="img" aria-label="Photo of a seaside villa with a pool and garden on the Costa del Sol"></div>
<div class="abs hero-title">
  <h1>High Tech Villa</h1>
  <p>412, Harbor Lane St. Portview<br>CA 40117</p>
</div>
<div class="abs ficon" style="top:254px"><svg width="24" height="24" viewBox="0 0 24 24" fill="none" stroke="#fff" stroke-width="1.6"><circle cx="12" cy="8" r="4"/><path d="M4 21c0-4 4-6 8-6s8 2 8 6z"/></svg></div>
<div class="abs ficon" style="top:336px"><svg width="24" height="24" viewBox="0 0 24 24" fill="none" stroke="#fff" stroke-width="1.6"><rect x="3" y="6" width="18" height="12"/><path d="M3 6l9 7 9-7"/></svg></div>
<div class="abs ficon" style="top:420px"><svg width="24" height="24" viewBox="0 0 24 24" fill="none" stroke="#fff" stroke-width="1.6"><rect x="4" y="5" width="16" height="15"/><path d="M4 10h16M8 3v4M16 3v4"/></svg></div>
<div class="abs ficon" style="top:502px"><svg width="24" height="24" viewBox="0 0 24 24" fill="none" stroke="#fff" stroke-width="1.6"><path d="M4 5h16v11H10l-4 4v-4H4z"/></svg></div>
<form class="abs consult">
  <div class="consult-head"><b>Request</b> Free<br>Consultation</div>
  <label style="left:46px;top:96px">YOUR NAME</label>
  <div class="field" style="left:46px;top:118px;width:250px">xxxxxxxx</div>
  <label style="left:46px;top:180px">EMAIL ADDRESS</label>
  <div class="field" style="left:46px;top:202px;width:250px">Enter Email</div>
  <label style="left:46px;top:262px">DATE</label>
  <label style="left:176px;top:262px">TIME</label>
  <div class="field" style="left:46px;top:286px;width:120px"></div>
  <div class="field" style="left:176px;top:286px;width:120px"></div>
  <label style="left:46px;top:346px">MESSAGE</label>
  <div class="field" style="left:46px;top:370px;width:250px"></div>
  <div class="consult-submit">Submit Now</div>
</form>

<div class="abs notice">
  <svg width="22" height="22" viewBox="0 0 24 24"><path fill="#0d1440" d="M12 2l3 7h7l-5.6 4.4 2.1 7.6L12 16.6 5.5 21l2.1-7.6L2 9h7z"/></svg>
  Solvista implements features like favorites, compare properties, advanced search fields. For more information check out <a>full list of features.</a>
</div>

<div class="abs ph-house" role="img" aria-label="Photo of a modern white three-storey house with trees"></div>
<div class="abs ph-frame" style="left:56px;top:805px;width:254px;height:436px"></div>
<div class="abs kicker" style="left:360px;top:815px">A Few Words About House</div>
<div class="abs section-title" style="left:360px;top:834px">Apartt Luxuary Villa</div>
<div class="abs rule" style="left:360px;top:872px;width:74px"></div>
<p class="abs body-text" style="left:360px;top:888px;width:790px">Neque porro quisquam est, qui dolorem ipsum quia dolor sit amet, consectetur, adipisci velit, sed quia non numquam eius modi tempora incidunt ut labore et dolore magnam aliquam quaerat voluptatem. Ut enim ad minima veniam, quis nostrum exercitationem ullam corporis suscipit laboriosam.</p>
<p class="abs body-text" style="left:360px;top:974px;width:790px">Neque porro quisquam est, qui dolorem ipsum quia dolor sit amet, consectetur, adipisci velit, sed quia non numquam eius modi tempora incidunt ut labore et dolore magnam aliquam.</p>
<div class="abs" style="left:360px;top:1064px;width:790px;height:1px;background:#ddd"></div>
<div class="abs room" style="left:362px;top:1100px">
  <svg width="44" height="48" viewBox="0 0 44 48" fill="#0d1440"><path d="M14 4h16v4H14z"/><path d="M8 8h28a4 4 0 0 1 4 4v4H4v-4a4 4 0 0 1 4-4z"/><g><circle cx="10" cy="24" r="2"/><circle cx="18" cy="24" r="2"/><circle cx="26" cy="24" r="2"/><circle cx="34" cy="24" r="2"/><circle cx="14" cy="32" r="2"/><circle cx="22" cy="32" r="2"/><circle cx="30" cy="32" r="2"/><circle cx="10" cy="40" r="2"/><circle cx="18" cy="40" r="2"/><circle cx="26" cy="40" r="2"/><circle cx="34" cy="40" r="2"/></g></svg>
  <div class="lbl">BATHROOM</div><div class="num">2</div></div>
<div class="abs room" style="left:534px;top:1100px">
  <svg width="50" height="48" viewBox="0 0 50 48" fill="#0d1440"><path d="M6 8h38v16H6z"/><rect x="11" y="14" width="11" height="8" fill="#fff"/><rect x="28" y="14" width="11" height="8" fill="#fff"/><path d="M2 26h46v12H2z"/><path d="M4 38h4v6H4zM42 38h4v6h-4z"/></svg>
  <div class="lbl">BEDROOM</div><div class="num">3</div></div>
<div class="abs room" style="left:706px;top:1100px">
  <svg width="50" height="48" viewBox="0 0 50 48" fill="#0d1440"><path d="M4 14h42v20H4z"/><rect x="9" y="18" width="32" height="8" fill="#fff"/><path d="M6 34h4v6H6zM40 34h4v6h-4z"/></svg>
  <div class="lbl">KIDSROOM</div><div class="num">1</div></div>
<div class="abs room" style="left:878px;top:1100px">
  <svg width="50" height="48" viewBox="0 0 50 48" fill="#0d1440"><path d="M8 6h34v30H8z"/><rect x="13" y="11" width="24" height="7" fill="#fff"/><path d="M6 36h38v4H6z"/></svg>
  <div class="lbl">GUESTROOM</div><div class="num">2</div></div>

<div class="abs ph-bedroom" role="img" aria-label="Photo of a bright bedroom with red bedding and lounge chairs"></div>
<div class="abs hl-bg"></div>
<div class="abs section-title" style="left:534px;top:1346px;color:var(--ink)">Property Highlights</div>
<div class="abs rule" style="left:534px;top:1394px;width:102px"></div>
<svg class="abs pin" style="left:524px;top:1430px" viewBox="0 0 38 48"><path fill="#333" d="M19 0a19 19 0 0 1 19 19c0 14-19 29-19 29S0 33 0 19A19 19 0 0 1 19 0z"/><rect x="12" y="13" width="14" height="10" fill="none" stroke="#fff" stroke-width="1.6"/></svg>
<div class="abs hl-item" style="left:578px;top:1432px"><h4>Paying Guest</h4><p>Lorem ipsum dolor sit amet, consec-teturin ligula convallis, vel tincidunt ipsum posusollicitudin.</p></div>
<svg class="abs pin" style="left:822px;top:1430px" viewBox="0 0 38 48"><path fill="#333" d="M19 0a19 19 0 0 1 19 19c0 14-19 29-19 29S0 33 0 19A19 19 0 0 1 19 0z"/><path d="M11 20l8-7 8 7v7H11z" fill="none" stroke="#fff" stroke-width="1.6"/></svg>
<div class="abs hl-item" style="left:872px;top:1436px"><h4>Buying and Selling</h4><p>Lorem ipsum dolor sit amet, consec-teturin ligula convallis, vel tincidunt ipsum posusollicitudin.</p></div>
<svg class="abs pin" style="left:530px;top:1558px" viewBox="0 0 38 48"><path fill="#333" d="M19 0a19 19 0 0 1 19 19c0 14-19 29-19 29S0 33 0 19A19 19 0 0 1 19 0z"/><path d="M11 16h16M12 26h14M14 18v7M19 18v7M24 18v7" stroke="#fff" stroke-width="1.6"/></svg>
<div class="abs hl-item" style="left:584px;top:1560px"><h4>Finance Service</h4><p>Lorem ipsum dolor sit amet, consec-teturin ligula convallis, vel tincidunt ipsum posusollicitudin.</p></div>
<svg class="abs pin" style="left:836px;top:1556px" viewBox="0 0 38 48"><path fill="#333" d="M19 0a19 19 0 0 1 19 19c0 14-19 29-19 29S0 33 0 19A19 19 0 0 1 19 0z"/><path d="M11 20l8-7 8 7v7H11z" fill="none" stroke="#fff" stroke-width="1.6"/></svg>
<div class="abs hl-item" style="left:882px;top:1556px"><h4>Legal Advice</h4><p>Lorem ipsum dolor sit amet, consec-teturin ligula convallis, vel tincidunt ipsum posusollicitudin.</p></div>

<div class="abs center kicker" style="top:1762px">House Features</div>
<div class="abs center section-title" style="top:1780px;color:var(--ink)">Room Dimensions</div>
<div class="abs rule" style="left:550px;top:1820px;width:100px"></div>
<p class="abs center body-text" style="top:1836px;padding:0 150px">Neque porro quisquam est, qui dolorem ipsum quia dolor sit amet, consectetur, adipisci velit, sed quia non numquam eius modi tempora incidunt ut labore et dolore magnam aliquam quaerat voluptatem. Ut enim ad minima veniam, quis nostrum exercitationem.</p>
<div class="abs ph-balcony" role="img" aria-label="Photo of a sunset balcony terrace with sofas overlooking the sea"></div>
<div class="abs ph-frame" style="left:110px;top:1934px;width:564px;height:345px"></div>
<div class="abs size-tag">14.5 x 12</div>
<div class="abs balcony-box">
  <h3>Balcony Bay</h3>
  <p>sed quia non numquam eius modi tempora incidunt ut labore et dolore magnam aliquam quaerat voluptatem. Ut enim ad minima veniam quis.</p>
  <ul><li>MOUNTAIN AND SEA VIEW</li><li>GOOD SENERY WITH LARGE VIEW</li><li>NEAT AND CLEAN ATMOSPHERE</li></ul>
</div>

<section class="abs contact">
  <div class="abs ph-agent" style="top:45px" role="img" aria-label="Portrait photo of the property agent"></div>
  <div class="abs w" style="left:373px;top:70px;font-size:14px">For Any Querry</div>
  <div class="abs w" style="left:373px;top:92px;font-size:24px">Contact Our Agent</div>
  <div class="abs" style="left:373px;top:132px;width:104px;height:2px;background:#fff"></div>
  <div class="abs w" style="left:373px;top:170px;font-size:15px;font-weight:700">Westbrook Valley</div>
  <div class="abs w" style="left:373px;top:226px;font-size:14px;line-height:28px">(Keystone Certified Agent)<br>Phone : 555-210-3380<br>Email : info@lumohabitat.com</div>
  <div class="abs w" style="left:793px;top:64px;font-size:18px">Send Message To Clara</div>
</section>
<div class="abs cf" style="top:2483px">NAME</div>
<div class="abs cf" style="top:2529px">EMAIL</div>
<div class="abs cf" style="top:2576px">PHONE</div>
<div class="abs cf" style="top:2622px;height:82px">MESSAGE</div>
<div class="abs send">Send</div>

<div class="abs map" role="img" aria-label="Map overview of the Costa del Sol coast showing the areas where properties are sold"></div>

<footer class="abs footer">
  <div class="abs brand-f"><span class="mark"></span><span class="name">Lumo Habitat</span></div>
  <div class="abs copy">© 2016 Lumo Habitat. All Rights Reserved.</div>
</footer>

</body>
</html>
```